business card with 2 locations on 1 card

I need a modern looking business card that I would use at 2 different locations. Possibly 1 location on 1 side and other location on other side. One should be able to distinguish the 2 locations immediately before having to read the address or description on card. You can take a look at my website to see what I'm drawn to. The logo is brand new that I just purchased on Craft Hive. I want to emphasize family.
Updates

Let's not use the yellow and blue colors. Added Thursday, August 31, 2017

Target Market(s)

women and children

Industry/Entity Type

Health And Wellness

Contact Information for Business Card

Business name: Willow Brook Chiropractic & Acupuncture
My name: Lorin Daske
Job title: DC, MSOM, LAC (NM), CNS

Location 1
Address: 4817 Marlowe Blvd, Suite C-210, Halverton, TX 75490
Phone: (469) 555-0182
Fax: (972) 555-0137

Location 2
Address: 1936 Belvane Road, Suite 140, Ardell, TX 75321
Phone: (469) 555-0169
Fax: (972) 555-0137

Email: drlorindaske@mailnest.example
Website: www.drlorindaske.example

Font styles to use
Serif
Sans Serif

Colors

Designer to choose colors to be used in the design.

Requirements
Must have
• distinction between 2 locations.
Nice to have
• Colors preference below is there. But I like to see what you come up with too!

```html
<!DOCTYPE html>
<html lang="en">
<head>
<meta charset="utf-8">
<title>Willow Brook Chiropractic &amp; Acupuncture — Business Card</title>
<link rel="stylesheet" href="https://fonts.googleapis.com/css2?family=Cinzel:wght@600;700&family=Roboto:wght@400;500;700&display=swap">
<style>
  :root {
    --backdrop: #262626;
    --paper: #f1f1f1;
    --teal: #2e6e6c;
    --green: #07831f;
    --green-mid: #1f9a2b;
    --lime: #b9e78b;
    --ink: #555555;
    --ink-strong: #3a3a3a;
    --white: #ffffff;
  }
  * { box-sizing: border-box; margin: 0; padding: 0; }
  html, body { width: 1200px; height: 960px; overflow: hidden; }
  body { background: var(--backdrop); position: relative; font-family: "Roboto", Arial, sans-serif; }

  .card { position: absolute; width: 600px; height: 342px; border-radius: 22px; overflow: hidden; }

  /* Front */
  .card-front { left: 302px; top: 129px; background: var(--paper); }
  .front-band {
    position: absolute; left: 0; top: 34px; width: 100%; height: 99px;
    background: linear-gradient(90deg, var(--teal) 0%, var(--teal) 68%, var(--green) 78%, var(--green) 100%);
  }
  .brand-dot {
    position: absolute; left: 417px; top: 32px; width: 104px; height: 104px; border-radius: 50%;
    background: var(--white);
  }
  .holder { position: absolute; left: 32px; top: 50px; color: var(--white); }
  .holder-name { font-family: "Cinzel", Georgia, serif; font-weight: 700; font-size: 23px; letter-spacing: .5px; line-height: 1; }
  .holder-title { font-size: 15px; font-weight: 500; margin-top: 5px; }
  .holder-email { font-size: 14px; margin-top: 3px; }

  .front-brand {
    position: absolute; right: 41px; top: 139px; text-align: right;
    font-family: "Cinzel", Georgia, serif; font-weight: 600; color: var(--teal); line-height: 1;
  }
  .front-brand .brand-main { display: block; font-size: 24px; }
  .front-brand .brand-sub { display: block; font-size: 11.5px; margin-top: 3px; }

  .location { position: absolute; top: 236px; font-size: 14.5px; color: var(--ink); line-height: 18px; font-style: normal; }
  .location-first { left: 32px; }
  .location-second { right: 39px; text-align: right; top: 238px; }
  .location .contact { margin-top: 6px; }
  .location b { color: var(--ink-strong); font-weight: 700; }

  /* Back */
  .card-back {
    left: 299px; top: 488px;
    background: linear-gradient(90deg, var(--teal) 0%, var(--teal) 18%, var(--green) 38%, var(--green-mid) 58%, var(--lime) 100%);
  }
  .back-mark { position: absolute; left: 233px; top: 79px; }
  .back-brand {
    position: absolute; left: 0; width: 100%; top: 219px; text-align: center;
    font-family: "Cinzel", Georgia, serif; font-weight: 600; color: var(--white); line-height: 1;
  }
  .back-brand .brand-main { display: block; font-size: 30px; }
  .back-brand .brand-sub { display: block; font-size: 14px; margin-top: 4px; }
</style>
</head>
<body>
  <section class="card card-front">
    <div class="front-band"></div>
    <div class="brand-dot"></div>
    <div class="holder">
      <h1 class="holder-name">LORIN DASKE</h1>
      <p class="holder-title">DC, MSOM, LAC (NM), CNS</p>
      <p class="holder-email">drlorindaske@mailnest.example</p>
    </div>
    <p class="front-brand">
      <span class="brand-main">Willow Brook</span>
      <span class="brand-sub">Chiropractic &amp; Acupuncture</span>
    </p>
    <address class="location location-first">
      <p>4817 Marlowe Blvd<br>Suite C-210, Halverton, TX 75490</p>
      <p class="contact"><b>P</b>: (469) 555-0182<br><b>F</b>: (972) 555-0137</p>
    </address>
    <address class="location location-second">
      <p>1936 Belvane Road<br>Suite 140, Ardell, TX 75321</p>
      <p class="contact"><b>P</b>: (469) 555-0169<br><b>F</b>: (972) 555-0137</p>
    </address>
  </section>

  <section class="card card-back">
    <svg class="back-mark" width="134" height="134" viewBox="0 0 134 134" aria-hidden="true">
      <circle cx="67" cy="67" r="62" fill="none" stroke="var(--white)" stroke-width="6"/>
    </svg>
    <p class="back-brand">
      <span class="brand-main">Willow Brook</span>
      <span class="brand-sub">Chiropractic &amp; Acupuncture</span>
    </p>
  </section>
</body>
</html>
```